VELMIR needs a more polished Packaging Design

VELMIR is a medical device company needing a new look for their packaging design.
• Please refer to File 3 in the attachments to find the template of the current package design.

We want the design to be clean and sophisticated. The logo must not be changed.
• Our Velmir logo can be found in File 1 and 2 in the attachments

Industry/Entity Type

It Company

```html
<!DOCTYPE html>
<html lang="en">
<head>
<meta charset="utf-8">
<title>VELMIR – Lens Carton Dieline</title>
<link rel="stylesheet" href="https://fonts.googleapis.com/css2?family=Michroma&family=Open+Sans:wght@400;600&display=swap">
<style>
  :root{
    --bg:#ffffff;
    --cut:#c9cdd2;
    --panel-blue:#a9e9f9;
    --panel-green:#ddf5b3;
    --brand-blue:#3cc6ef;
    --ink:#7f93a0;
    --ink-dark:#5c6e7a;
    --icon:#8a98a2;
  }
  html,body{margin:0;padding:0;width:1200px;height:1000px;overflow:hidden;background:var(--bg);}
  .carton{display:block;width:1200px;height:1000px;}
  .cut-line{fill:none;stroke:var(--cut);stroke-width:1;}
  .fold-line{stroke:var(--cut);stroke-width:1;}
  .fill-blue{fill:var(--panel-blue);}
  .fill-green{fill:var(--panel-green);}
  .fill-white{fill:#fff;}
  .brand-name{font-family:"Michroma",sans-serif;fill:var(--brand-blue);}
  .tech-copy{font-family:"Michroma",sans-serif;fill:var(--ink);letter-spacing:.04em;}
  .fine-copy{font-family:"Open Sans",sans-serif;fill:var(--ink-dark);font-size:4.6px;}
  .lang-code{font-family:"Open Sans",sans-serif;font-weight:600;fill:var(--ink);font-size:6px;}
  .lang-box{fill:#fff;stroke:#d3dde3;stroke-width:.6;}
  .icon{fill:none;stroke:var(--icon);stroke-width:.9;}
  .icon-label{font-family:"Open Sans",sans-serif;fill:var(--icon);font-size:6px;}
</style>
</head>
<body>
<svg class="carton" viewBox="0 0 1200 1000" xmlns="http://www.w3.org/2000/svg" aria-label="VELMIR lens carton dieline">
  <g transform="translate(290,-60)">

    <!-- colour fills -->
    <rect class="fill-blue" x="236" y="120" width="274" height="665"/>
    <rect class="fill-blue" x="90" y="145" width="550" height="50"/>
    <rect class="fill-white" x="176" y="145" width="60" height="25"/>
    <rect class="fill-white" x="510" y="170" width="45" height="25"/>
    <rect class="fill-blue" x="176" y="220" width="334" height="195"/>
    <rect class="fill-green" x="22" y="415" width="488" height="47"/>
    <rect class="fill-green" x="236" y="785" width="274" height="85"/>

    <!-- cut outline -->
    <path class="cut-line" d="M176 210 L176 130 Q176 120 186 120 L545 120 Q555 120 555 130 L555 210
             M176 210 L100 210 L90 200 L90 150 L100 140 L176 140
             M555 140 L630 140 L640 150 L640 200 L630 210 L555 210
             M176 220 L40 220 Q22 220 22 238 L22 462 Q22 480 40 480 L176 480
             M555 220 L640 220 L640 480 L555 480
             M176 490 L100 490 L90 500 L90 570 L100 580 L176 580
             M555 490 L630 490 L640 500 L640 570 L630 580 L555 580
             M176 870 L176 985 Q176 1000 191 1000 L540 1000 Q555 1000 555 985 L555 870"/>
    <line class="fold-line" x1="176" y1="210" x2="176" y2="870"/>
    <line class="fold-line" x1="555" y1="210" x2="555" y2="870"/>
    <line class="fold-line" x1="176" y1="215" x2="555" y2="215"/>
    <line class="fold-line" x1="22" y1="220" x2="176" y2="220"/>
    <line class="fold-line" x1="176" y1="485" x2="555" y2="485"/>
    <line class="fold-line" x1="176" y1="580" x2="555" y2="580"/>
    <line class="fold-line" x1="75" y1="220" x2="75" y2="480"/>
    <line class="fold-line" x1="600" y1="220" x2="600" y2="480"/>
    <line class="fold-line" x1="176" y1="870" x2="555" y2="870"/>

    <!-- top lid (upside down) -->
    <text class="tech-copy" font-size="6.4" transform="translate(398,157) rotate(180)" textLength="215" lengthAdjust="spacingAndGlyphs">HYDROPHILIC ACRYLIC INTRAOCULAR LENS</text>
    <rect class="fill-white" x="410" y="145" width="100" height="30"/>
    <text class="brand-name" font-size="14" text-anchor="middle" transform="translate(460,154) rotate(180)">VELMIR</text>

    <!-- front panel -->
    <text class="brand-name" x="373" y="388" font-size="42" text-anchor="middle">VELMIR</text>
    <text class="tech-copy" font-size="8">
      <tspan x="248" y="432">CONTENTS:  ONE HYDROPHILIC ACRYLIC</tspan>
      <tspan x="248" y="444">INTRAOCULAR LENS WITH 360° SQUARE</tspan>
      <tspan x="248" y="456">EDGE</tspan>
    </text>

    <!-- left side panel -->
    <text class="brand-name" font-size="20" transform="translate(153,268) rotate(-90)" text-anchor="middle">VELMIR</text>

    <!-- right side panel icons -->
    <g transform="translate(572,0)">
      <text class="icon-label" transform="translate(0,252) rotate(90)">Single</text>
      <text class="icon-label" transform="translate(-8,252) rotate(90)">Use Only</text>
      <circle class="icon" cx="0" cy="292" r="6"/><path class="icon" d="M-4 288 L4 296 M4 288 L-4 296"/>
      <circle class="icon" cx="0" cy="326" r="6"/><path class="icon" d="M-4 322 L4 330"/>
      <circle class="icon" cx="0" cy="358" r="6"/><path class="icon" d="M-4 354 L4 362"/>
      <path class="icon" d="M-6 390 L6 384 L6 396 Z"/>
      <rect class="icon" x="-5" y="414" width="10" height="28"/>
    </g>

    <!-- bottom panel: company details -->
    <g class="tech-copy" font-size="5.8">
      <text x="248" y="520">NORTHLIGHT OPTICAL SYSTEMS LTD.</text>
      <text x="248" y="530" textLength="250" lengthAdjust="spacingAndGlyphs">HARROW HOUSE, HARROW AVENUE, ASHBY, WESTSHIRE</text>
      <text x="248" y="540">AB1 2CD, UNITED KINGDOM</text>
      <text x="248" y="550" textLength="250" lengthAdjust="spacingAndGlyphs">WEBSITE: WWW.NL-OPTICS.COM   E-MAIL: INFO@NL-OPTICS.COM</text>
    </g>
    <text class="tech-copy" x="498" y="568" font-size="5.6" text-anchor="end">REV.06 E0503062015</text>

    <!-- back panel -->
    <rect class="fill-white" x="236" y="592" width="110" height="33"/>
    <text class="brand-name" x="291" y="614" font-size="15" text-anchor="middle">VELMIR</text>

    <g class="lang-list">
      <rect class="lang-box" x="245" y="651" width="14" height="11"/><text class="lang-code" x="248" y="659">UK</text>
      <text class="fine-copy"><tspan x="264" y="655">Contains one sterile lens</tspan><tspan x="264" y="661">Do not use if damaged</tspan><tspan x="264" y="667">Do not resterilize</tspan></text>
      <rect class="lang-box" x="245" y="680" width="14" height="11"/><text class="lang-code" x="248" y="688">DN</text>
      <text class="fine-copy"><tspan x="264" y="684">Indeholder en steril linse</tspan><tspan x="264" y="690">Brug ikke hvis beskadiget</tspan></text>
      <rect class="lang-box" x="245" y="697" width="14" height="11"/><text class="lang-code" x="248" y="705">FR</text>
      <text class="fine-copy"><tspan x="264" y="701">Contient une lentille stérile</tspan><tspan x="264" y="707">Ne pas utiliser si endommagé</tspan></text>
      <rect class="lang-box" x="245" y="714" width="14" height="11"/><text class="lang-code" x="248" y="722">GE</text>
      <text class="fine-copy"><tspan x="264" y="718">Enthält eine sterile Linse</tspan><tspan x="264" y="724">Nicht verwenden wenn beschädigt</tspan></text>

      <rect class="lang-box" x="378" y="651" width="14" height="11"/><text class="lang-code" x="380" y="659">GR</text>
      <text class="fine-copy"><tspan x="397" y="655">Περιέχει ένα στείρο φακό</tspan><tspan x="397" y="661">Μη χρησιμοποιείτε αν έχει φθορά</tspan></text>
      <rect class="lang-box" x="378" y="680" width="14" height="11"/><text class="lang-code" x="382" y="688">IT</text>
      <text class="fine-copy"><tspan x="397" y="684">Contiene una lente sterile</tspan><tspan x="397" y="690">Non usare se danneggiata</tspan></text>
      <rect class="lang-box" x="378" y="697" width="14" height="11"/><text class="lang-code" x="380" y="705">PO</text>
      <text class="fine-copy"><tspan x="397" y="701">Contém uma lente estéril</tspan><tspan x="397" y="707">Não usar se danificada</tspan></text>
      <rect class="lang-box" x="378" y="714" width="14" height="11"/><text class="lang-code" x="380" y="722">SP</text>
      <text class="fine-copy"><tspan x="397" y="718">Contiene una lente estéril</tspan><tspan x="397" y="724">No usar si está dañado</tspan></text>
    </g>

    <!-- back panel icons -->
    <g class="icon-row">
      <rect class="icon" x="297" y="824" width="30" height="10"/>
      <path class="icon" d="M350 822 L357 835 L343 835 Z"/>
      <circle class="icon" cx="378" cy="829" r="6"/><path class="icon" d="M374 825 L382 833"/>
      <circle class="icon" cx="407" cy="829" r="6"/><path class="icon" d="M403 825 L411 833 M411 825 L403 833"/>
      <circle class="icon" cx="437" cy="829" r="6"/><path class="icon" d="M433 825 L441 833 M441 825 L433 833"/>
      <text class="icon-label"><tspan x="447" y="828">Single</tspan><tspan x="447" y="835">Use Only</tspan></text>
    </g>
  </g>
</svg>
</body>
</html>
```